Design Home Screen

We’re looking for talented UI/UX designers to create an eye-popping, modern, and fun Home Screen for the Plenk app — the future of real-time earned wage access and financial empowerment.
Your mission: make the Plenk experience come alive the moment users open the app.

Design Goals

The screen should instantly communicate energy, financial control, and trust.

The “Time on the Clock” and the “Plenk Balance” must be the stars of the screen — presented in a way that feels alive, interactive, and rewarding.

Think of how to visually celebrate a user’s progress at work and their earnings — something that makes checking the app feel fun and satisfying, not transactional.

Creative Direction

Style: Sleek, fintech-modern, with motion or visual elements that feel alive (micro-animations, glowing accents, gradient depth, or movement cues).

Tone: Confident, vibrant, and optimistic — this is a financial app that feels human and inspiring.

Color palette: Black, Gold, and Green, and any other color.

Typography: Clean, readable, and balanced between playful and professional.

Must-Have Elements

Time on the Clock – creatively displayed (e.g., countdown or progress animation as the user works).

Plenk Balance – bold, fun, and maybe even interactive (reflecting growth as the user earns).

A clean navigation structure for core tabs: Home, Access Pay, Boost, History, Profile.

Engaging micro-animations, icons, or progress indicators that make the user feel “in motion.”

Room for brand personality — the “Plenk” name and logo if desired.

```html
<!DOCTYPE html>
<html lang="en">
<head>
<meta charset="utf-8">
<title>Plenk – Home</title>
<link href="https://fonts.googleapis.com/css2?family=Poppins:wght@400;500;600;700&display=swap" rel="stylesheet">
<style>
  :root{
    --navy:#1f3a5b;
    --navy-deep:#172f4b;
    --ink:#111111;
    --white:#ffffff;
    --gold:#d9b547;
    --blue:#4f86c6;
    --bell:#5d8fc6;
    --card-bg:#f4f8fc;
    --card-line:#5a93c6;
    --panel:#eef4fa;
    --rule:#c9d3dc;
    --avatar:#0e72a5;
    --icon:#0f5d8e;
  }
  *{margin:0;padding:0;box-sizing:border-box}
  html,body{width:1200px;height:2600px;overflow:hidden;background:var(--white)}
  body{font-family:'Poppins',sans-serif;color:var(--ink);position:relative}
  .abs{position:absolute}

  .header{left:0;top:0;width:1200px;height:768px;border-radius:0 0 88px 88px;
    background:radial-gradient(ellipse at 80% 30%,#2a4a70 0%,var(--navy) 55%,var(--navy-deep) 100%);color:var(--white)}
  .status-time{left:36px;top:22px;font-size:44px;font-weight:500}
  .status-icons{left:1020px;top:30px}
  .avatar{left:26px;top:119px;width:151px;height:139px;border-radius:10px;
    background:linear-gradient(160deg,#c9ccd1,#6d7683)}
  .hello{left:203px;top:138px;font-size:29px;font-weight:500}
  .user-name{left:203px;top:172px;font-size:43px;font-weight:500}
  .brand{left:0;width:1200px;top:118px;text-align:center;font-size:70px;font-weight:700}
  .filter{left:988px;top:152px}
  .bell{left:1090px;top:142px;width:93px;height:93px;border-radius:16px;background:var(--bell);
    display:flex;align-items:center;justify-content:center}
  .label{font-size:43px;font-weight:400}
  .balance-label{left:64px;top:322px}
  .balance{left:58px;top:384px;font-size:118px;font-weight:600;line-height:1.1}
  .period-label{left:64px;top:582px;font-size:41px}
  .period{left:64px;top:642px;font-size:47px;font-weight:700}
  .hours-label{left:644px;top:322px}
  .hours-box{left:638px;top:412px;width:478px;height:151px}
  .hours-text{left:638px;top:412px;width:478px;height:151px;display:flex;align-items:center;justify-content:center;font-size:58px;font-weight:500}
  .rate{left:644px;top:594px;font-size:40px}
  .rate small{font-size:33px}
  .clock-state{left:644px;top:644px;font-size:50px;font-weight:600}

  .action{top:858px;height:276px;border:3px solid var(--card-line);border-radius:28px;background:var(--card-bg);
    display:flex;flex-direction:column;align-items:center;padding-top:22px}
  .action svg{height:130px}
  .action span{margin-top:18px;font-size:35px;line-height:1.4;text-align:center;font-weight:400}

  .panel{left:0;top:1203px;width:1200px;height:1397px;background:var(--panel);border-radius:40px 40px 0 0}
  .panel-title{left:35px;top:1244px;font-size:47px;font-weight:600}
  .range{left:922px;top:1250px;width:249px;height:75px;border:3px solid #9fb6cc;border-radius:14px;background:#dbe7f2;
    display:flex;align-items:center;justify-content:space-between;padding:0 26px 0 28px;font-size:38px}
  .rule{left:35px;width:1130px;height:4px;background:var(--rule)}
  .row{left:0;width:1200px;height:270px}
  .row .initials{position:absolute;left:32px;top:33px;width:205px;height:205px;border-radius:50%;background:var(--avatar);
    color:var(--white);display:flex;align-items:center;justify-content:center;font-size:78px;font-weight:500}
  .row .payee{position:absolute;left:273px;top:50px;font-size:44px;font-weight:600}
  .row .date{position:absolute;left:273px;top:140px;font-size:37px}
  .row .amount{position:absolute;right:44px;top:50px;font-size:45px;font-weight:600}
  .row .method{position:absolute;right:44px;top:140px;font-size:37px}

  .nav{left:29px;top:2430px;width:1146px;height:145px;border-radius:28px;background:var(--navy);
    display:flex;align-items:center;padding-left:9px}
  .nav-home{width:287px;height:122px;border-radius:22px;background:var(--white);display:flex;align-items:center;justify-content:center;gap:26px;
    font-size:43px;font-weight:500}
  .nav-icon{position:absolute;top:2450px}
</style>
</head>
<body>

<section class="header abs">
  <div class="status-time abs">7:41</div>
  <svg class="status-icons abs" width="150" height="50" viewBox="0 0 150 50" fill="#fff">
    <rect x="4" y="30" width="8" height="14" rx="1"/><rect x="16" y="22" width="8" height="22" rx="1"/>
    <rect x="28" y="14" width="8" height="30" rx="1"/><rect x="40" y="6" width="8" height="38" rx="1"/>
    <rect x="74" y="8" width="56" height="36" rx="5" fill="none" stroke="#fff" stroke-width="4"/>
    <rect x="80" y="14" width="44" height="24" rx="2"/><rect x="132" y="19" width="6" height="14" rx="2"/>
  </svg>

  <div class="avatar abs" role="img" aria-label="Profile photo of the user"></div>
  <div class="hello abs">Hello!</div>
  <div class="user-name abs">Sam Rivera</div>
  <div class="brand abs">Plenk</div>

  <svg class="filter abs" width="70" height="70" viewBox="0 0 70 70" fill="none" stroke="#fff" stroke-width="4" stroke-linecap="round">
    <line x1="8" y1="16" x2="62" y2="16"/><line x1="8" y1="35" x2="62" y2="35"/><line x1="8" y1="54" x2="62" y2="54"/>
    <circle cx="44" cy="16" r="6" fill="var(--navy)"/><circle cx="24" cy="35" r="6" fill="var(--navy)"/><circle cx="40" cy="54" r="6" fill="var(--navy)"/>
  </svg>
  <div class="bell abs">
    <svg width="56" height="60" viewBox="0 0 56 60" fill="#fff">
      <path d="M28 4c-11 0-18 8-18 19v13l-6 9h48l-6-9V23C46 12 39 4 28 4z"/>
      <circle cx="28" cy="51" r="7"/>
    </svg>
  </div>

  <div class="label balance-label abs">Plenk Wage Balance:</div>
  <div class="balance abs">$10</div>
  <div class="period-label abs">Current Pay Period:</div>
  <div class="period abs">MARCH 1 - 15, 2025</div>

  <div class="label hours-label abs">Work Hours:</div>
  <svg class="hours-box abs" viewBox="0 0 478 151" fill="none" stroke-width="9">
    <path d="M194 5H26Q5 5 5 26V125Q5 146 26 146H240" stroke="var(--gold)"/>
    <path d="M194 5H452Q473 5 473 26V125Q473 146 452 146H240" stroke="var(--blue)"/>
    <circle cx="194" cy="5" r="16" fill="#8aa5c2" stroke="var(--gold)" stroke-width="5"/>
  </svg>
  <div class="hours-text abs">19:00 HRS.</div>
  <div class="rate abs">Status: <small>@ $20.00/hr</small></div>
  <div class="clock-state abs">On the Clock</div>
</section>

<div class="action abs" style="left:26px;width:270px">
  <svg viewBox="0 0 130 130" fill="none" stroke="var(--icon)" stroke-width="5" stroke-linecap="round" stroke-linejoin="round">
    <rect x="12" y="14" width="106" height="56" rx="4"/>
    <circle cx="65" cy="42" r="12"/><circle cx="32" cy="42" r="3" fill="var(--icon)"/><circle cx="98" cy="42" r="3" fill="var(--icon)"/>
    <path d="M65 80v34M52 102l13 13 13-13"/><line x1="34" y1="122" x2="96" y2="122"/>
  </svg>
  <span>Request<br>Money</span>
</div>
<div class="action abs" style="left:316px;width:270px">
  <svg viewBox="0 0 130 130" fill="none" stroke="var(--icon)" stroke-width="5" stroke-linecap="round" stroke-linejoin="round">
    <path d="M52 36V24a13 13 0 0 1 26 0"/><rect x="42" y="36" width="46" height="38" rx="6"/>
    <circle cx="65" cy="55" r="9"/>
    <path d="M14 92l20-12c8-5 16-4 24 0l14 6c5 2 4 9-2 9H54"/><path d="M14 120l22-8h34l40-26c5-3 11 3 6 8l-30 30"/>
  </svg>
  <span>Loan<br>Access</span>
</div>
<div class="action abs" style="left:606px;width:273px">
  <svg viewBox="0 0 130 130" fill="none" stroke="var(--icon)" stroke-width="5" stroke-linecap="round" stroke-linejoin="round">
    <circle cx="58" cy="30" r="16"/><path d="M42 24h32"/>
    <path d="M22 118V80c0-12 10-20 22-20h28c12 0 20 8 20 20"/><path d="M52 62l6 18 6-18"/>
    <rect x="74" y="86" width="44" height="32" rx="4"/><path d="M88 86v-6h16v6"/>
  </svg>
  <span>Update<br>Employment</span>
</div>
<div class="action abs" style="left:899px;width:275px">
  <svg viewBox="0 0 130 130" fill="none" stroke="var(--icon)" stroke-width="5" stroke-linecap="round" stroke-linejoin="round">
    <rect x="8" y="50" width="78" height="42" rx="4" transform="rotate(-14 47 71)"/>
    <rect x="14" y="66" width="80" height="44" rx="4"/><circle cx="54" cy="88" r="9"/>
    <ellipse cx="106" cy="32" rx="16" ry="16"/><ellipse cx="106" cy="82" rx="16" ry="6"/>
    <path d="M90 58v24M122 58v24M90 70c0 3 7 6 16 6s16-3 16-6"/><ellipse cx="106" cy="58" rx="16" ry="6"/>
  </svg>
  <span>Earn<br>$7,500</span>
</div>

<section class="panel abs"></section>
<div class="panel-title abs">Transaction</div>
<div class="range abs">Weekly
  <svg width="34" height="22" viewBox="0 0 34 22" fill="none" stroke="#111" stroke-width="4" stroke-linecap="round"><path d="M4 4l13 13L30 4"/></svg>
</div>
<div class="rule abs" style="top:1355px"></div>

<div class="row abs" style="top:1364px">
  <div class="initials">SR</div><div class="payee">Rivera Works Inc.</div><div class="date">July 12, 2025</div>
  <div class="amount">$350.50</div><div class="method">Sent | Via PayLoop</div>
</div>
<div class="rule abs" style="top:1631px"></div>
<div class="row abs" style="top:1633px">
  <div class="initials">L</div><div class="payee">Larana Inc.</div><div class="date">July 12, 2025</div>
  <div class="amount">$280.75</div><div class="method">Sent | Via PayLoop</div>
</div>
<div class="rule abs" style="top:1900px"></div>
<div class="row abs" style="top:1902px">
  <div class="initials">G</div><div class="payee">Gigwell</div><div class="date">July 12, 2025</div>
  <div class="amount">$350.50</div><div class="method">Sent | Via PayLoop</div>
</div>
<div class="rule abs" style="top:2170px"></div>
<div class="row abs" style="top:2172px">
  <div class="initials">FG</div><div class="payee">Fernhill Goods</div><div class="date">July 12, 2025</div>
  <div class="amount">$350.50</div><div class="method">Sent | Via PayLoop</div>
</div>

<nav class="nav abs">
  <div class="nav-home">
    <svg width="62" height="60" viewBox="0 0 62 60" fill="var(--navy)"><path d="M31 4L4 26v30h20V38h14v18h20V26z"/></svg>
    Home
  </div>
</nav>
<svg class="nav-icon abs" style="left:403px" width="76" height="104" viewBox="0 0 76 104" fill="none" stroke="#fff" stroke-width="4" stroke-linecap="round">
  <rect x="16" y="6" width="44" height="92" rx="8"/><line x1="32" y1="14" x2="44" y2="14"/>
  <path d="M30 40c4 4 4 16 0 20M38 36c6 6 6 22 0 28M46 32c8 8 8 28 0 36"/>
  <path d="M8 38c-4 8-4 20 0 28M68 38c4 8 4 20 0 28"/>
</svg>
<svg class="nav-icon abs" style="left:600px" width="104" height="104" viewBox="0 0 104 104" fill="none" stroke="#fff" stroke-width="4" stroke-linecap="round" stroke-linejoin="round">
  <path d="M40 64L30 54c14-30 34-44 64-46-2 30-16 50-46 64z"/><circle cx="66" cy="38" r="8"/>
  <path d="M30 54l-16-2 14-16h18M48 72l2 16 16-14V56"/><path d="M22 76l-12 18M30 84l-8 14M18 66l-10 10"/>
</svg>
<svg class="nav-icon abs" style="left:812px" width="104" height="104" viewBox="0 0 104 104" fill="none" stroke="#fff" stroke-width="4" stroke-linecap="round" stroke-linejoin="round">
  <path d="M50 96H22V8h44l18 18v26"/><path d="M66 8v18h18"/>
  <line x1="34" y1="34" x2="58" y2="34"/><line x1="34" y1="48" x2="66" y2="48"/><line x1="34" y1="62" x2="48" y2="62"/>
  <circle cx="74" cy="76" r="18"/><path d="M74 66v10l7 5"/>
</svg>
<svg class="nav-icon abs" style="left:1025px" width="96" height="104" viewBox="0 0 96 104" fill="none" stroke="#fff" stroke-width="4">
  <circle cx="48" cy="32" r="22"/><path d="M10 98V86c0-14 12-24 26-24h24c14 0 26 10 26 24v12z"/>
</svg>

</body>
</html>
```